Brindle Advisory Business Card Design

Business card for business consulting company, using attached logo. We do financial and strategic consulting, and want a clean, professional image with a bit of fun. Our logo is a flat whale tail, which symbolizes the Orca whale, a highly collaborative, group based animal that is very successful in navigating the ocean, protecting the herd, and hunting. We like the logo that is blue and gray on white one one side, but would be open to a blue card with white lettering on the other side... or whatever you'd suggest
Updates
Hi all - I have had the logo modified to take the shadowing off the tail. I will post it on the brief... under a file name called updated logo. thank you Added Saturday, April 25, 2015
Target Market(s)
Small to medium sized businesses ($10M to $500M in revenue per year), financial and sales executives, general managers, attorneys and CPAs
Industry/Entity Type
Financial
Contact Information for Business Card
Want company name, contact info - name, title, telephone, email, website, linkedin, twitter and Facebook. No physical address yet.
Requirements
Must have
- contemporary design, bold, strong, confident but with a bit of fun. prominently feature the logo and the whale tail icon
Nice to have
- unique touches that would differentiate us from a regular card... for example, logo and writing all on front on white background, but on back - logo in white on a blue background
- open to idea of different shapes of card than standard... but not sure
Should not have
- ?

```html
<!DOCTYPE html>
<html lang="en">
<head>
<meta charset="utf-8">
<title>Brindle Advisory Business Card</title>
<link href="https://fonts.googleapis.com/css2?family=Open+Sans:wght@400;600;700&display=swap" rel="stylesheet">
<style>
  :root {
    --page-bg: #2e2f31;
    --navy: #1a3c6e;
    --navy-deep: #143259;
    --navy-light: #22508e;
    --white: #ffffff;
    --grey: #8a8d91;
    --rule: rgba(255, 255, 255, 0.18);
    --soft-white: rgba(255, 255, 255, 0.78);
  }
  * { margin: 0; padding: 0; box-sizing: border-box; }
  html, body {
    width: 1200px;
    height: 900px;
    overflow: hidden;
    background: var(--page-bg);
    font-family: "Open Sans", Arial, sans-serif;
  }
  .canvas {
    position: relative;
    width: 1200px;
    height: 900px;
    display: flex;
    justify-content: center;
    align-items: center;
    gap: 60px;
  }
  .card {
    position: relative;
    width: 360px;
    height: 630px;
    border-radius: 20px;
    overflow: hidden;
    box-shadow: 0 14px 34px rgba(0, 0, 0, 0.45);
  }

  /* Front */
  .card-front { background: var(--white); }
  .front-head {
    position: relative;
    height: 250px;
    display: flex;
    flex-direction: column;
    align-items: center;
    padding-top: 48px;
  }
  .brand-square {
    width: 150px;
    height: 122px;
    border-radius: 18px;
    background: var(--navy);
  }
  .wordmark {
    margin-top: 28px;
    font-size: 30px;
    font-weight: 600;
    letter-spacing: -0.5px;
    color: var(--navy);
    line-height: 1;
  }
  .tagline {
    align-self: flex-end;
    margin-right: 44px;
    margin-top: 4px;
    font-size: 10px;
    color: var(--grey);
  }
  .front-body {
    position: relative;
    height: 310px;
    background: var(--navy);
    color: var(--white);
    text-align: center;
    padding-top: 30px;
  }
  .front-body::before {
    content: "";
    position: absolute;
    top: 0;
    left: 50%;
    transform: translateX(-50%);
    border-left: 14px solid transparent;
    border-right: 14px solid transparent;
    border-top: 14px solid var(--white);
  }
  .person-name { font-size: 24px; font-weight: 400; letter-spacing: 0.5px; line-height: 1.1; }
  .person-title { font-size: 16px; margin-top: 2px; }
  .rule {
    width: 250px;
    height: 1px;
    margin: 20px auto;
    background: var(--rule);
  }
  .contact-line { font-size: 15px; line-height: 1.75; }
  .social-line {
    display: flex;
    justify-content: center;
    align-items: center;
    gap: 6px;
    font-size: 16px;
  }
  .social-square {
    width: 15px;
    height: 15px;
    background: var(--white);
    border-radius: 2px;
  }
  .front-foot {
    height: 70px;
    display: flex;
    align-items: center;
    justify-content: center;
    font-size: 17px;
    font-weight: 600;
    color: var(--navy);
  }

  /* Back */
  .card-back {
    background: radial-gradient(circle at 45% 35%, var(--navy-light) 0%, var(--navy) 45%, var(--navy-deep) 100%);
  }
  .back-square {
    position: absolute;
    top: 160px;
    left: 50%;
    transform: translateX(-50%);
    width: 170px;
    height: 150px;
    border-radius: 20px;
    background: var(--navy-light);
  }
  .back-url {
    position: absolute;
    bottom: 48px;
    width: 100%;
    text-align: center;
    font-size: 15px;
    color: var(--soft-white);
  }
</style>
</head>
<body>
<main class="canvas">
  <section class="card card-front" aria-label="Card front">
    <header class="front-head">
      <div class="brand-square"></div>
      <div class="wordmark">Brindle Advisory</div>
      <div class="tagline">business consulting</div>
    </header>
    <div class="front-body">
      <div class="person-name">YOUR NAME</div>
      <div class="person-title">Title</div>
      <div class="rule"></div>
      <div class="contact-line">P: 555 014 2290</div>
      <div class="contact-line">E: info@brindleadvisory.com</div>
      <div class="rule"></div>
      <div class="social-line"><span class="social-square"></span>/brindleadvisory</div>
    </div>
    <footer class="front-foot">www.brindleadvisory.com</footer>
  </section>

  <section class="card card-back" aria-label="Card back">
    <div class="back-square"></div>
    <div class="back-url">www.brindleadvisory.com</div>
  </section>
</main>
</body>
</html>
```